Business card design needed

I need a business card design for a dog walking, dog minding and dog training business. Please refer to my website for the basic company colours and fonts I'm after. Planning on a double sided card, so all information doesn't need to be on the 'front' side.
Cheers

Industry/Entity Type

Dog Training

Contact Information for Business Card

Meadow Paws - happy hounds
Rua 0498307164
meadowpawsdemo.com.au
-walking
-holiday stays
-onsite care
-training and behavioural consultations

```html
<!DOCTYPE html>
<html lang="en">
<head>
<meta charset="utf-8">
<title>Meadow Paws – Business Card</title>
<link rel="stylesheet" href="https://fonts.googleapis.com/css2?family=Alfa+Slab+One&family=Questrial&display=swap">
<style>
  :root {
    --canvas: #e4e8e8;
    --card-black: #1c1c1c;
    --strip-dark: #2a1f1d;
    --accent: #ea3f05;
    --white: #ffffff;
    --photo-tone: #e9e4df;
    --icon-tone: #f1ede8;
  }
  * { box-sizing: border-box; margin: 0; padding: 0; }
  html, body { width: 1200px; height: 1000px; overflow: hidden; }
  body {
    background: var(--canvas);
    position: relative;
    font-family: "Questrial", "Century Gothic", sans-serif;
  }
  .card {
    position: absolute;
    left: 300px;
    width: 600px;
    height: 340px;
    background: var(--card-black);
    overflow: hidden;
    box-shadow: 0 6px 18px rgba(0,0,0,0.18);
  }
  .card--front { top: 90px; }
  .card--back { top: 540px; }

  /* front */
  .front-stripe {
    position: absolute; left: 0; top: 0; bottom: 0; width: 44px;
    background: var(--accent);
    border-right: 1px dashed rgba(255,255,255,0.6);
  }
  .photo-frame {
    position: absolute; left: 232px; top: 22px;
    width: 216px; height: 216px; border-radius: 50%;
    background: var(--white);
    border: 5px solid var(--accent);
    display: flex; align-items: center; justify-content: center;
  }
  .photo-fill {
    width: 196px; height: 196px; border-radius: 50%;
    background: radial-gradient(circle at 50% 45%, var(--photo-tone), var(--white) 75%);
  }
  .web-address {
    position: absolute; left: 70px; right: 36px; bottom: 38px;
    text-align: right;
    font-family: "Alfa Slab One", "Rockwell", serif;
    font-size: 23px; letter-spacing: 0.5px;
    color: var(--white); text-transform: uppercase;
    white-space: nowrap;
  }

  /* back */
  .brand {
    position: absolute; left: 40px; top: 114px;
    display: flex; align-items: center; gap: 8px;
  }
  .brand-square { width: 20px; height: 20px; background: var(--accent); }
  .brand-name {
    font-size: 22px; color: var(--white); letter-spacing: 0.5px;
    text-transform: uppercase; white-space: nowrap;
  }
  .services {
    position: absolute; left: 320px; top: 60px; right: 0;
    list-style: none;
  }
  .service {
    display: flex; align-items: center; gap: 14px;
    height: 34px; margin-bottom: 18px;
    background: var(--strip-dark);
    color: var(--white); font-size: 18px;
  }
  .service-icon {
    width: 26px; height: 30px; border-radius: 3px;
    background: var(--icon-tone);
    margin-left: 6px;
  }
  .contact-band {
    position: absolute; left: 0; bottom: 0; width: 600px; height: 96px;
  }
  .phone {
    position: absolute; left: 0; right: 0; bottom: 26px;
    display: flex; justify-content: center; align-items: center; gap: 6px;
    color: var(--white); font-size: 16px; letter-spacing: 0.5px;
  }
</style>
</head>
<body>

  <section class="card card--front" aria-label="Card front">
    <div class="front-stripe"></div>
    <div class="photo-frame">
      <div class="photo-fill" role="img" aria-label="Photo of a small terrier sitting with a leash in its mouth"></div>
    </div>
    <p class="web-address">meadowpawsdemo.com.au</p>
  </section>

  <section class="card card--back" aria-label="Card back">
    <div class="brand">
      <span class="brand-square"></span>
      <span class="brand-name">Meadow Paws</span>
    </div>

    <ul class="services">
      <li class="service"><span class="service-icon" role="img" aria-label="Icon of a person walking a dog"></span>Dog walking</li>
      <li class="service"><span class="service-icon" role="img" aria-label="Icon of a person petting a dog"></span>Dog minding</li>
      <li class="service"><span class="service-icon" role="img" aria-label="Icon of a person training a dog"></span>Dog training</li>
    </ul>

    <svg class="contact-band" viewBox="0 0 600 96" aria-hidden="true">
      <path d="M0 36 H260 Q268 36 272 28 Q278 14 300 14 Q322 14 328 28 Q332 36 340 36 H600 V96 H0 Z" fill="var(--accent)"/>
      <path d="M0 42 H258 Q268 42 274 32 Q280 20 300 20 Q320 20 326 32 Q332 42 342 42 H600" fill="none" stroke="rgba(255,255,255,0.6)" stroke-width="1" stroke-dasharray="3 2"/>
      <path d="M0 88 H600" fill="none" stroke="rgba(255,255,255,0.6)" stroke-width="1" stroke-dasharray="3 2"/>
    </svg>
    <p class="phone">
      <svg width="14" height="14" viewBox="0 0 14 14" aria-hidden="true">
        <circle cx="7" cy="7" r="6" fill="none" stroke="var(--white)" stroke-width="1.3"/>
        <path d="M4.6 4 L5.8 3.8 L6.4 5.4 L5.7 6 Q6.3 7.4 7.8 8.2 L8.5 7.5 L10 8.1 L9.9 9.4 Q7.4 9.8 5.6 7.9 Q4 6.1 4.6 4 Z" fill="var(--white)"/>
      </svg>
      0498307164
    </p>
  </section>

</body>
</html>
```